Salt Water Delivery Company Business Card Design

We are a company that delivers natural saltwater (from the ocean) to aquarium companies, restaurants and home marine tanks. I would like a new business card to suit.

Must include Name, company name, abn, contact number and website as well as logo (see attached).

Looking for a design that stands out, has a clean but unique appearance.

Double and single sided entries welcome

Industry/Entity Type

Business

Requirements
Must have
• Logo

```html
<!DOCTYPE html>
<html lang="en">
<head>
<meta charset="utf-8">
<title>Brine Runner – Business Card</title>
<link rel="stylesheet" href="https://fonts.googleapis.com/css2?family=Open+Sans:wght@400;600;700;800&display=swap">
<style>
  :root {
    --stage: #1a1a1a;
    --card-blue: #2a6ff0;
    --band-light: #7fd2f6;
    --band-mid: #4fb2f2;
    --white: #ffffff;
  }
  * { margin: 0; padding: 0; box-sizing: border-box; }
  html, body { width: 1200px; height: 403px; overflow: hidden; background: var(--stage); }
  .stage { position: relative; width: 1200px; height: 403px; font-family: "Open Sans", Arial, sans-serif; color: var(--white); }
  .card {
    position: absolute; top: 55px; width: 525px; height: 299px;
    background: var(--card-blue); border-radius: 18px; overflow: hidden;
  }
  .card--front { left: 58px; }
  .card--back { left: 628px; }

  .card__band {
    position: absolute; left: 0; right: 0; bottom: 0; height: 34px;
    background: linear-gradient(90deg, var(--band-light), var(--band-mid));
  }

  .brand { position: absolute; display: flex; flex-direction: column; align-items: flex-start; }
  .brand__row { display: flex; align-items: center; gap: 10px; }
  .brand__dot { width: 22px; height: 22px; border-radius: 50%; background: var(--white); }
  .brand__name { font-weight: 800; font-size: 38px; line-height: 1; color: var(--white); letter-spacing: -0.5px; }
  .brand__tagline { font-weight: 600; font-size: 15px; color: var(--white); margin: 6px 0 0 32px; }
  .card--front .brand { left: 66px; top: 58px; }
  .card--back .brand { left: 118px; top: 120px; }

  .person { position: absolute; left: 92px; top: 158px; font-size: 18px; }
  .person__name { font-weight: 700; }
  .person__title { font-weight: 400; font-size: 16px; }

  .contacts { position: absolute; left: 90px; top: 197px; list-style: none; font-size: 12.5px; line-height: 20px; }
  .contacts li { display: flex; align-items: center; gap: 5px; }
  .contacts svg { width: 11px; height: 11px; }

  .company { position: absolute; right: 13px; top: 231px; text-align: right; font-size: 12.5px; line-height: 19px; }
  .company__name { font-weight: 700; }

  .back-web { position: absolute; left: 0; right: 0; top: 238px; text-align: center; font-size: 16px; letter-spacing: 3.5px; }
</style>
</head>
<body>
<div class="stage">
  <section class="card card--front">
    <div class="card__band" role="img" aria-label="Light blue wave band along the bottom of the card"></div>
    <div class="brand">
      <div class="brand__row"><span class="brand__dot"></span><span class="brand__name">Brine Runner</span></div>
      <span class="brand__tagline">Saltwater Deliveries</span>
    </div>
    <p class="person"><span class="person__name">Your name,</span> <span class="person__title">Title</span></p>
    <ul class="contacts">
      <li><svg viewBox="0 0 12 12"><circle cx="6" cy="6" r="5.5" fill="none" stroke="#fff"/><path d="M4 3.5 L5 3.5 L5.5 5 L4.8 5.6 C5.2 6.5 5.6 6.9 6.4 7.2 L7 6.5 L8.5 7 L8.5 8 C6 8.5 3.5 6 4 3.5Z" fill="#fff"/></svg>123-456-7890</li>
      <li><svg viewBox="0 0 12 12"><circle cx="6" cy="6" r="5.5" fill="#fff"/></svg>www.website.com</li>
      <li>ABN : 0123456789</li>
    </ul>
    <div class="company">
      <p class="company__name">Brine Runner LLC</p>
      <p>Street Name, City Name</p>
      <p>State, City Zip Code</p>
    </div>
  </section>

  <section class="card card--back">
    <div class="brand">
      <div class="brand__row"><span class="brand__dot"></span><span class="brand__name">Brine Runner</span></div>
      <span class="brand__tagline">Saltwater Deliveries</span>
    </div>
    <p class="back-web">www.website.com</p>
  </section>
</div>
</body>
</html>
```